Flyer for Makeup Class

A flyer for my makeup class promotion. I am a make up artist starting a group class to teach makeup to ladies. I have attached some verbiage handwritten. My picture is the one in pink hijab. I have also attached some inspiration ideas and color combination (the colors in the cake design are the ones I want to use).

Target Market(s)

Ladies looking to learn make up from a make up artist

Industry/Entity Type

Hair And Beauty

Requirements
Must have
• The verbiage / description that I have hand written should be written using graphics and nice fonts. You can change the exact wording to make it better.

```html
<!DOCTYPE html>
<html lang="en">
<head>
<meta charset="utf-8">
<title>Makeup Master Class Flyer</title>
<link href="https://fonts.googleapis.com/css2?family=Barlow:wght@300;500&family=Open+Sans:wght@400;600&family=Archivo:wght@600;800&display=swap" rel="stylesheet">
<style>
  :root {
    --page-bg: #eeeeee;
    --pink-light: #f6d6d8;
    --pink-mid: #eeaebb;
    --pink-deep: #e07594;
    --hijab: #f3c3bd;
    --hijab-shade: #e9aaa6;
    --magenta: #b8407e;
    --red: #c8102e;
    --navy: #2b3a4e;
    --white: #ffffff;
    --title-ink: #26384c;
  }
  * { margin: 0; padding: 0; box-sizing: border-box; }
  html, body { width: 1200px; height: 1200px; overflow: hidden; background: var(--page-bg); }
  .flyer {
    position: absolute; left: 176px; top: 0;
    width: 848px; height: 1200px; overflow: hidden;
    background: var(--pink-light);
  }
  .backdrop {
    position: absolute; inset: 0 0 380px 0;
    background:
      radial-gradient(circle at 20% 8%, rgba(232,90,140,.55), transparent 22%),
      radial-gradient(circle at 85% 10%, rgba(232,90,140,.5), transparent 20%),
      radial-gradient(circle at 92% 45%, rgba(236,120,160,.45), transparent 14%),
      linear-gradient(180deg, var(--pink-mid) 0%, var(--pink-light) 45%, #f2dcd8 100%);
  }
  .portrait {
    position: absolute; left: 30px; top: 300px; width: 500px; height: 500px;
    border-radius: 250px 250px 0 0;
    background:
      radial-gradient(ellipse at 50% 30%, var(--hijab) 0%, var(--hijab) 34%, transparent 35%),
      radial-gradient(ellipse at 50% 75%, var(--hijab-shade) 0%, var(--hijab) 40%, transparent 41%),
      linear-gradient(180deg, rgba(240,190,195,.6) 0%, rgba(233,170,170,.7) 60%, var(--magenta) 100%);
  }
  .bands { position: absolute; inset: 0; }
  .title {
    position: absolute; top: 80px; width: 100%; text-align: center;
    font-family: "Barlow", sans-serif; color: var(--title-ink); line-height: .95;
  }
  .title-top { display: block; font-size: 84px; font-weight: 500; letter-spacing: 1px; }
  .title-bottom { display: block; font-size: 80px; font-weight: 300; letter-spacing: 2px; }
  .byline { position: absolute; left: 540px; top: 340px; font-family: "Archivo", sans-serif; color: var(--title-ink); font-weight: 800; }
  .byline-by { font-size: 28px; }
  .byline-name { font-size: 34px; margin-top: 12px; }
  .byline-role { font-size: 13px; font-weight: 600; }
  .details { position: absolute; left: 60px; top: 810px; color: var(--white); font-family: "Open Sans", sans-serif; }
  .venue-label { font-size: 36px; }
  .venue-place { font-size: 22px; line-height: 1.2; margin-left: 6px; }
  .event-date { font-size: 42px; margin-top: 8px; line-height: 1.1; }
  .event-time { font-size: 34px; line-height: 1.1; }
  .summary { font-family: "Archivo", sans-serif; font-weight: 600; font-size: 17px; width: 420px; margin-top: 22px; line-height: 1.2; }
  .audience { position: absolute; left: 510px; top: 860px; color: var(--white); }
  .audience-title { font-family: "Barlow", sans-serif; font-weight: 300; font-size: 40px; letter-spacing: 1px; }
  .audience-list { list-style: none; margin-top: 10px; font-family: "Archivo", sans-serif; font-weight: 600; font-size: 22px; }
  .audience-list li { display: flex; align-items: center; gap: 14px; height: 36px; }
  .tick { width: 26px; height: 22px; }
  .booking { position: absolute; right: 50px; top: 1070px; text-align: right; color: var(--white); font-family: "Archivo", sans-serif; font-weight: 800; font-size: 22px; line-height: 1.4; }
  .contact { position: absolute; top: 1135px; left: 300px; display: flex; align-items: center; gap: 40px; color: var(--white); }
  .phones { display: flex; align-items: center; gap: 14px; font-family: "Open Sans", sans-serif; font-size: 24px; line-height: 1.1; }
  .phone-icon { width: 34px; height: 40px; }
  .social { display: flex; align-items: center; gap: 12px; font-family: "Open Sans", sans-serif; font-size: 18px; }
  .social-dot { width: 30px; height: 30px; border-radius: 50%; background: var(--white); }
</style>
</head>
<body>
<main class="flyer">
  <div class="backdrop" aria-hidden="true"></div>
  <div class="portrait" role="img" aria-label="Portrait of the makeup artist in a pink hijab and magenta top, looking to the side"></div>

  <svg class="bands" width="848" height="1200" viewBox="0 0 848 1200" aria-hidden="true">
    <polygon points="0,748 310,800 848,738 848,1200 0,1200" fill="var(--navy)"/>
    <polygon points="0,768 310,820 848,760 848,1045 0,1150" fill="var(--red)"/>
  </svg>

  <h1 class="title">
    <span class="title-top">EXCLUSIVE MAKEUP</span>
    <span class="title-bottom">MASTER CLASS</span>
  </h1>

  <div class="byline">
    <div class="byline-by">By</div>
    <div class="byline-name">SAMIRA HADI</div>
    <div class="byline-role">(UK BASED MUA)</div>
  </div>

  <section class="details">
    <div class="venue-label">VENUE:</div>
    <div class="venue-place">Lakeside Club Complex<br>(Northgate)</div>
    <div class="event-date">6th April 2019</div>
    <div class="event-time">11:30 - 5:30 pm</div>
    <p class="summary">This Class is packed with loads of information tips, live demos, goodie bag, certificate, Q &amp; A, Lunch and much more</p>
  </section>

  <section class="audience">
    <h2 class="audience-title">PERFECT FOR</h2>
    <ul class="audience-list">
      <li><svg class="tick" viewBox="0 0 26 22"><path d="M2 12 L10 19 L24 3" fill="none" stroke="var(--white)" stroke-width="5" stroke-linecap="round" stroke-linejoin="round"/></svg>Professionals,</li>
      <li><svg class="tick" viewBox="0 0 26 22"><path d="M2 12 L10 19 L24 3" fill="none" stroke="var(--white)" stroke-width="5" stroke-linecap="round" stroke-linejoin="round"/></svg>Beginners</li>
      <li><svg class="tick" viewBox="0 0 26 22"><path d="M2 12 L10 19 L24 3" fill="none" stroke="var(--white)" stroke-width="5" stroke-linecap="round" stroke-linejoin="round"/></svg>and makeup lovers</li>
    </ul>
  </section>

  <div class="booking">To Book your Place<br>Contact</div>

  <div class="contact">
    <div class="phones">
      <svg class="phone-icon" viewBox="0 0 24 28"><path d="M6 1 C3 2 1 5 2 9 C4 17 9 24 16 27 C19 28 22 26 23 23 L18 19 L15 21 C12 19 9 14 8 10 L11 8 L9 2 Z" fill="var(--white)"/></svg>
      <div>01700123456<br>03000987654</div>
    </div>
    <div class="social">
      <span class="social-dot"></span>
      <span>@samirahadibeauty</span>
    </div>
  </div>
</main>
</body>
</html>
```